Business Card,

Keystone Ridge & Holdings LLC (DBA Bramble Dwellings) is a licensed residential contractor in Southwest Louisiana, specializing in custom homes, remodels, additions, and Fortified Gold roof systems.

We’re looking for a designer who can capture the look and feel of a modern, trustworthy Southern-style builder — a brand that communicates craftsmanship, class, and confidence at a glance.

This design package will be used for client meetings, door-to-door marketing, and online advertising, so we need visuals that stand out both in-hand and on screen.

Target Market(s)

Ages 30–65 Married or family-oriented Household income $85,000+ Own or are purchasing a home and want upgrades, additions, or complete rebuilds Value craftsmanship, reliability, and financing flexibility ($0 down options) Respond well to clear before/after visuals, trust-based branding, and professional presentation 🧠 Design cue: They’re not looking for the cheapest contractor — they want someone they can trust with their home and their money. Designs should look professional, clean, and confident.

Industry/Entity Type

Residential Construction, Custom Home Building & Remodeling

Contact Information for Business Card

Logo, "Bramble Dwellings", “Proudly serving Southwest Louisiana with Quality Craftsmanship & Financing Options”, Full Name + Title Dorian Plack Licensed Residential Contractor | LA #413968, Financing Options QR Code, Phone :337-582-9037 Email: Dorian@brambledwellings.net, Website: www.keystoneridgebuilders.homes , Service Area: Lake Charles & Surrounding Areas ,“Fully Licensed & Insured” ,A small 5-star icon with “Rated 5 Stars by Local Homeowners” , “Schedule Your Free Design-Build Starter Session Today!”

Font styles to use
Other font styles liked:
• Montserrat Bold for business name, Lora Italic for tagline, open sans regular for contact info,

Colors
0054AA
0677BA
7BADD7
CADEEF
E8F1F8

Requirements
Must have
• (Deep Navy (#1 Color) and Gold or rich metallic accent color) “$0 Down Financing Available” and the QR Code Name, Title, and direct Contact Info, Custom Homes • Additions • Remodels • Fortified Roofing
Nice to have
• 5 Star Google Icon, “Refer a friend — Earn $500 when they build with us.”, Facebook.com/keystoneridge
Should not have
• Don’t Cram 10 services, slogans, or contact details. Don’t Mix random colors or fonts to “stand out.”, Don’t Use hammer or roof clip art., Don’t Use script, gothic, or cursive fonts., Don’t Add loud textures or frames.

```html
<!DOCTYPE html>
<html lang="en">
<head>
<meta charset="utf-8">
<title>Bramble Dwellings – Business Card</title>
<link rel="stylesheet" href="https://fonts.googleapis.com/css2?family=Montserrat:wght@600;700&family=Open+Sans:wght@400;600;700&display=swap">
<style>
  :root {
    --backdrop: #d9d9d6;
    --card-black: #050505;
    --gold-dark: #a87a1c;
    --gold-mid: #e2b63f;
    --gold-light: #f6dc7a;
    --gold-text: #d6a934;
    --ink: #0b0b0b;
    --gold-band: linear-gradient(90deg, var(--gold-dark) 0%, var(--gold-mid) 30%, var(--gold-light) 55%, var(--gold-mid) 75%, var(--gold-dark) 100%);
  }
  * { box-sizing: border-box; margin: 0; padding: 0; }
  html, body { width: 1200px; height: 1000px; overflow: hidden; }
  body {
    background: var(--backdrop);
    display: flex;
    align-items: center;
    justify-content: center;
    gap: 40px;
    font-family: "Open Sans", sans-serif;
  }
  .card {
    position: relative;
    width: 560px;
    height: 320px;
    background: var(--card-black);
    overflow: hidden;
    box-shadow: 0 10px 26px rgba(0,0,0,.25);
  }
  .gold-band { position: absolute; left: 0; right: 0; background: var(--gold-band); }

  /* contact side */
  .contact-card .top-band { top: 30px; height: 32px; }
  .contact-card .name {
    position: absolute; top: 30px; left: 32px; height: 32px; line-height: 32px;
    font-family: "Montserrat", sans-serif; font-weight: 700; font-size: 22px;
    letter-spacing: .5px; color: var(--ink); text-transform: uppercase;
  }
  .contact-card .title {
    position: absolute; top: 70px; left: 32px;
    font-size: 12px; color: var(--gold-text);
  }
  .contact-list { position: absolute; top: 104px; left: 32px; list-style: none; }
  .contact-list li {
    display: flex; align-items: center; gap: 9px;
    font-size: 12px; line-height: 22px; color: var(--gold-text);
  }
  .contact-list svg { width: 12px; height: 12px; fill: var(--gold-text); flex: none; }
  .trust {
    position: absolute; right: 34px; top: 196px; text-align: center;
    color: var(--gold-text); font-size: 12.5px; line-height: 1.3;
  }
  .stars { display: flex; gap: 4px; justify-content: center; margin: 5px 0 3px; }
  .stars svg { width: 17px; height: 17px; fill: var(--gold-mid); }
  .cta {
    position: absolute; left: 32px; bottom: 30px;
    font-size: 12.5px; font-weight: 600; color: var(--gold-text);
  }
  .contact-card .bottom-band { bottom: 10px; height: 14px; }

  /* brand side */
  .brand-card .top-band { top: 24px; height: 22px; }
  .brand-card .bottom-band { bottom: 22px; height: 24px; }
  .brand-card .tagline {
    position: absolute; left: 0; right: 0; bottom: 22px; height: 24px; line-height: 24px;
    text-align: center; font-size: 11px; font-weight: 600; color: var(--ink);
  }
  .brand-lockup {
    position: absolute; left: 0; right: 0; top: 128px;
    display: flex; align-items: center; justify-content: center; gap: 14px;
  }
  .brand-mark { width: 22px; height: 22px; background: var(--gold-mid); }
  .brand-name {
    font-family: "Montserrat", sans-serif; font-weight: 600; font-size: 30px;
    letter-spacing: 2px; color: var(--gold-mid); text-transform: uppercase;
  }
</style>
</head>
<body>

  <section class="card contact-card">
    <div class="gold-band top-band"></div>
    <h1 class="name">Dorian Plack</h1>
    <p class="title">Licensed Residential Contractor</p>
    <ul class="contact-list">
      <li><svg viewBox="0 0 24 24"><path d="M12 2a7 7 0 0 0-7 7c0 5 7 13 7 13s7-8 7-13a7 7 0 0 0-7-7zm0 9.5A2.5 2.5 0 1 1 12 6.5a2.5 2.5 0 0 1 0 5z"/></svg>LA #413968 Financing</li>
      <li><svg viewBox="0 0 24 24"><path d="M6.6 10.8a15 15 0 0 0 6.6 6.6l2.2-2.2a1 1 0 0 1 1-.25 11.4 11.4 0 0 0 3.6.57 1 1 0 0 1 1 1V20a1 1 0 0 1-1 1A17 17 0 0 1 3 4a1 1 0 0 1 1-1h3.5a1 1 0 0 1 1 1c0 1.25.2 2.45.57 3.57a1 1 0 0 1-.25 1z"/></svg>337-582-9037</li>
      <li><svg viewBox="0 0 24 24"><path d="M2 5h20v14H2zm2 2v.5l8 5 8-5V7z"/></svg>Dorian@brambledwellings.net</li>
      <li><svg viewBox="0 0 24 24"><circle cx="12" cy="12" r="10"/></svg>www.keystoneridgebuilders.homes</li>
    </ul>
    <div class="trust">
      <p>Fully Licensed &amp; Insured</p>
      <div class="stars" aria-label="5 stars">
        <svg viewBox="0 0 24 24"><path d="M12 2l3 7 7.5.6-5.7 4.9 1.8 7.5L12 18l-6.6 4 1.8-7.5L1.5 9.6 9 9z"/></svg>
        <svg viewBox="0 0 24 24"><path d="M12 2l3 7 7.5.6-5.7 4.9 1.8 7.5L12 18l-6.6 4 1.8-7.5L1.5 9.6 9 9z"/></svg>
        <svg viewBox="0 0 24 24"><path d="M12 2l3 7 7.5.6-5.7 4.9 1.8 7.5L12 18l-6.6 4 1.8-7.5L1.5 9.6 9 9z"/></svg>
        <svg viewBox="0 0 24 24"><path d="M12 2l3 7 7.5.6-5.7 4.9 1.8 7.5L12 18l-6.6 4 1.8-7.5L1.5 9.6 9 9z"/></svg>
        <svg viewBox="0 0 24 24"><path d="M12 2l3 7 7.5.6-5.7 4.9 1.8 7.5L12 18l-6.6 4 1.8-7.5L1.5 9.6 9 9z"/></svg>
      </div>
      <p>by Local Homeowners</p>
    </div>
    <p class="cta">Schedule Your Free Design-Build Starter Session Today!</p>
    <div class="gold-band bottom-band"></div>
  </section>

  <section class="card brand-card">
    <div class="gold-band top-band"></div>
    <div class="brand-lockup">
      <span class="brand-mark"></span>
      <span class="brand-name">Bramble Dwellings</span>
    </div>
    <div class="gold-band bottom-band"></div>
    <p class="tagline">Proudly serving Southwest Louisiana with Quality Craftsmanship &amp; Financing</p>
  </section>

</body>
</html>
```